New website

Our website (www.larchvale.com) needs to be replaced with something gorgeous and glossy. We do like the text of our current website but have many new images to put on the site. We want to create a website that shows viewers what our team can do, and how we can create something amazing for them and their homes.

Coding

```html
<!DOCTYPE html>
<html lang="en">
<head>
<meta charset="utf-8">
<title>Larchvale Landscaping</title>
<link rel="stylesheet" href="https://fonts.googleapis.com/css2?family=Ubuntu:wght@400;500;700&family=Open+Sans:wght@400;600;700&display=swap">
<style>
:root{
  --navy:#141c52;
  --navy-deep:#0f1a45;
  --navy-field:#2b306b;
  --green:#4cb860;
  --green-dark:#3a9d4c;
  --bg-soft:#f5f6f8;
  --text:#6b6f7d;
  --white:#ffffff;
  --footer:#0c0f14;
  --orange:#e8692d;
}
*{margin:0;padding:0;box-sizing:border-box}
html,body{width:1200px;height:4183px;overflow:hidden}
body{position:relative;font-family:"Open Sans",sans-serif;color:var(--text);background:var(--white)}
.abs{position:absolute}
h1,h2,h3,h4{font-family:"Ubuntu",sans-serif;font-weight:500}
.btn{position:absolute;background:var(--green);color:var(--white);font-family:"Ubuntu",sans-serif;font-weight:500;display:flex;align-items:center;justify-content:center;gap:18px}

/* top bar */
.updates{top:0;left:0;width:1200px;height:54px;background:#f4f4f6;display:flex;align-items:center;justify-content:center;font-size:12.5px;color:#555}
.updates b{color:var(--orange);margin:0 6px 0 10px;font-weight:700}
.updates .ic{width:14px;height:11px;border:1.5px solid var(--green);border-radius:2px}

/* nav */
.nav{top:54px;left:0;width:1200px;height:68px;background:var(--white)}
.brand{position:absolute;left:32px;top:18px;font-family:"Ubuntu",sans-serif;font-size:22px;letter-spacing:4px;color:#555a66;text-transform:uppercase}
.brand-sub{position:absolute;left:32px;top:46px;font-size:8px;letter-spacing:6px;color:#8a8f99}
.nav-links a{position:absolute;top:26px;font-size:11.5px;font-weight:700;color:var(--navy);text-decoration:none;letter-spacing:.2px}
.nav-links a.active{color:var(--green)}
.nav-rule{position:absolute;left:224px;top:0;width:1px;height:68px;background:#e6e6ea}
.call{position:absolute;left:966px;top:10px;width:48px;height:48px;border-radius:50%;background:#444;display:flex;align-items:center;justify-content:center}
.call-label{position:absolute;left:1028px;top:15px;font-size:11px;font-weight:700;color:var(--green)}
.call-num{position:absolute;left:1028px;top:34px;font-size:15px;font-weight:700;color:var(--navy)}

/* hero */
.hero-photo{top:122px;left:0;width:1200px;height:700px;background:linear-gradient(90deg,#1c2550 0%,#2c3a44 30%,#4f6a3a 55%,#6f8a44 80%,#587636 100%)}
.hero-title{left:114px;top:305px;font-size:42px;line-height:48px;color:var(--white)}
.hero-text{left:114px;top:422px;width:420px;font-size:18px;line-height:27px;color:var(--white)}
.hero-btn{left:114px;top:528px;width:144px;height:40px;border-radius:20px;font-size:12px;font-family:"Open Sans",sans-serif;font-weight:700}

/* about */
.about{top:828px;left:0;width:1200px;height:564px;background:var(--bg-soft)}
.eyebrow{position:absolute;font-size:13px;font-weight:600;color:var(--green);text-transform:uppercase;padding-bottom:4px;border-bottom:2px solid var(--green)}
.about-ring{left:98px;top:896px;width:444px;height:444px;border-radius:50%;background:#555a8a}
.about-photo{left:122px;top:895px;width:424px;height:444px;border-radius:50%;background:radial-gradient(circle at 60% 45%,#5f8a3e,#2f5a28 70%,#23421f)}
.about-badge{left:437px;top:1226px;width:98px;height:98px;border-radius:50%;background:var(--white);box-shadow:0 4px 14px rgba(0,0,0,.12);display:flex;align-items:center;justify-content:center}
.about h2{position:absolute;left:617px;top:942px;font-size:42px;line-height:53px;color:var(--navy)}
.about h3{position:absolute;left:617px;top:1072px;font-size:24px;color:var(--navy);font-weight:400}
.about p{position:absolute;left:617px;top:1116px;width:505px;font-size:13px;line-height:21.8px}
.about-btn{left:619px;top:1275px;width:154px;height:44px;font-size:16px}

/* services */
.section-head{position:absolute;left:0;width:1200px;text-align:center}
.section-head h2{font-size:42px;color:var(--navy);margin-top:18px}
.service{position:absolute;top:1605px;width:321px;height:344px;overflow:hidden}
.service .photo{position:absolute;inset:0}
.service .cap{position:absolute;left:0;bottom:0;width:100%;height:46px;background:rgba(20,28,82,.55);color:var(--white);font-family:"Ubuntu",sans-serif;font-weight:700;font-size:20px;text-align:center;line-height:44px}
.service .cap-ic{position:absolute;left:50%;bottom:30px;margin-left:-40px;width:80px;height:40px;border-radius:40px 40px 0 0;background:rgba(20,28,82,.55);display:flex;justify-content:center;padding-top:8px}
.service.featured .photo{background:var(--navy)}
.service.featured h3{position:absolute;top:172px;width:100%;text-align:center;color:var(--white);font-weight:700;font-size:20px}
.service.featured p{position:absolute;top:212px;left:42px;width:237px;text-align:center;color:#e5e7f0;font-size:13.5px;line-height:21px}

/* help band */
.help{top:2025px;left:0;width:1200px;height:422px;background:linear-gradient(90deg,#222a58,#2d3460 60%,#3a4066)}
.help-circle{left:690px;top:2095px;width:438px;height:438px;border-radius:50%;background:rgba(255,255,255,.08)}
.help-photo{left:740px;top:2082px;width:440px;height:365px;background:linear-gradient(160deg,#9a8d6c,#7b6b4e 50%,#3f5a2e);border-radius:40% 0 0 0}
.help h2{position:absolute;left:101px;top:2100px;font-size:52px;line-height:63px;color:var(--white);font-weight:700}
.help p{position:absolute;left:101px;top:2240px;width:520px;font-size:23px;line-height:34px;color:var(--white)}
.help-btn{left:106px;top:2338px;width:155px;height:45px;font-size:16px}

/* testimonials */
.reviews{top:2447px;left:0;width:1200px;height:566px;background:var(--bg-soft)}
.review{position:absolute;top:2644px;width:318px;height:182px;background:var(--white);border-radius:6px;box-shadow:0 6px 18px rgba(20,28,82,.06);padding:40px 20px 0 22px;font-size:16px;line-height:23px}
.review.active{background:var(--green);color:var(--white)}
.review .tail{position:absolute;left:0;bottom:-20px;width:0;height:0;border-top:20px solid var(--green);border-right:20px solid transparent}
.person{position:absolute;top:2858px}
.person .av{position:absolute;left:24px;top:0;width:56px;height:56px;border-radius:50%}
.person .nm{position:absolute;left:97px;top:4px;font-family:"Ubuntu",sans-serif;font-weight:500;font-size:15.5px;color:var(--navy);white-space:nowrap}
.person .nm.g{color:var(--green)}
.person .rl{position:absolute;left:97px;top:27px;font-size:12px;white-space:nowrap}
.dots{left:564px;top:2960px;display:flex;gap:5px;align-items:center}
.dots span{width:8px;height:8px;border-radius:50%;background:#aac9b6}
.dots span.on{width:24px;border-radius:4px;background:var(--navy)}

/* contact */
.form-box{left:112px;top:3266px;width:484px;height:359px;background:var(--navy-deep)}
.form-box h3{position:absolute;left:50px;top:40px;font-size:24px;color:var(--white);font-weight:700}
.form-box .dash{position:absolute;left:226px;top:57px;width:46px;height:2px;background:var(--green)}
.field{position:absolute;background:var(--navy-field);color:#d8dae8;font-size:12px;padding-left:18px;display:flex;align-items:center}
.quote-btn{left:50px;top:3556px;width:124px;height:38px;font-size:11px;font-family:"Open Sans",sans-serif;font-weight:700;gap:6px}
.contact-photo{left:596px;top:3282px;width:484px;height:331px;background:linear-gradient(160deg,#8fb86a,#4d7a36 45%,#6b5a3e 80%)}

/* footer */
.footer{top:3730px;left:0;width:1200px;height:453px;background:var(--footer)}
.foot-brand{left:142px;top:3950px;font-family:"Ubuntu",sans-serif;font-size:28px;letter-spacing:6px;color:#e8e8ea;text-transform:uppercase}
.foot-info{position:absolute;top:3950px;display:flex;gap:12px;align-items:flex-start;color:#e8e8ea;font-size:14px;line-height:19px}
.foot-sep{position:absolute;top:3948px;width:1px;height:48px;background:#555}
.foot-rule{position:absolute;left:258px;width:706px;height:1px;background:#555}
.foot-nav a{position:absolute;top:4053px;color:#e8e8ea;font-size:15px;text-decoration:none}
.copy{left:146px;top:4128px;color:#e8e8ea;font-size:13px}
.social{position:absolute;top:4124px;width:25px;height:25px;border:1.5px solid #e8e8ea;border-radius:3px}
</style>
</head>
<body>

<div class="abs updates"><span class="ic"></span><b>UPDATES:</b>Lorem ipsum dolor sit amet, consectetur adipiscing elit, sed do eiusmod tempor incididunt ut labore et dolore magna aliqua.</div>

<header class="abs nav">
  <div class="brand">Larchvale</div>
  <div class="brand-sub">LANDSCAPING</div>
  <div class="nav-rule"></div>
  <nav class="nav-links">
    <a class="active" style="left:248px">HOME</a>
    <a style="left:323px">ABOUT US</a>
    <a style="left:415px">SERVICES</a>
    <a style="left:502px">OUR TEAM</a>
    <a style="left:605px">CONTACT US</a>
  </nav>
  <div class="call"><svg width="22" height="22" viewBox="0 0 24 24"><path fill="#fff" d="M6.6 10.8a15.1 15.1 0 0 0 6.6 6.6l2.2-2.2c.3-.3.7-.4 1-.2 1.1.4 2.3.6 3.6.6.6 0 1 .4 1 1V20c0 .6-.4 1-1 1A17 17 0 0 1 3 4c0-.6.4-1 1-1h3.5c.6 0 1 .4 1 1 0 1.3.2 2.5.6 3.6.1.3 0 .7-.2 1z"/></svg></div>
  <div class="call-label">ENQURIES</div>
  <div class="call-num">+ 1-800-555-01-47</div>
</header>

<section>
  <div class="abs hero-photo" role="img" aria-label="Gardener in work overalls pushing a lawn mower across a green garden"></div>
  <h1 class="abs hero-title">Landscaping Solutions You<br>Can Count On.</h1>
  <p class="abs hero-text">Lorem ipsum dolor sit amet, consectetur adip iscing elit, sed do eiusmod tempor incididunt ut labore et dolore</p>
  <a class="btn hero-btn">READ MORE</a>
  <svg class="abs" style="left:0;top:730px" width="1200" height="110" viewBox="0 0 1200 110">
    <path d="M0 70 C250 20 450 30 650 70 C850 110 1000 90 1200 40 L1200 110 L0 110Z" fill="var(--green)"/>
    <path d="M0 78 C250 30 450 40 650 82 C850 124 1000 104 1200 58 L1200 110 L0 110Z" fill="var(--bg-soft)"/>
  </svg>
</section>

<section class="abs about">
  <span class="eyebrow" style="left:617px;top:80px">WHO WE ARE</span>
  <h2 style="top:114px">The team you can trust<br>to get the job done</h2>
  <h3 style="top:244px">Cultivating Beauty Outdoors</h3>
  <p style="top:288px">Lorem ipsum dolor sit amet, consectetur adipiscing elit, sed do eiusmod tempor incididunt ut labore et dolore magna aliqua. Ut enim ad minim veniam, quis nos trud exercitation ullamco laboris nisi ut aliquip ex ea commodo consequat.<br>Duis aute irure dolor in reprehenderit in voluptate velit esse cillum dolore eu fugiat nulla pariatur. Excepteur sint occaecat cupidatat non proident, sunt in culpa qui officia deserunt mollit anim id est laborum.</p>
</section>
<div class="abs about-ring"></div>
<div class="abs about-photo" role="img" aria-label="Gardener trimming a tall hedge with power shears"></div>
<div class="abs about-badge">
  <svg width="52" height="52" viewBox="0 0 52 52"><g stroke="var(--green)" stroke-width="4" stroke-linecap="round">
    <line x1="26" y1="4" x2="26" y2="12"/><line x1="26" y1="40" x2="26" y2="48"/><line x1="4" y1="26" x2="12" y2="26"/><line x1="40" y1="26" x2="48" y2="26"/>
    <line x1="10" y1="10" x2="16" y2="16"/><line x1="36" y1="36" x2="42" y2="42"/><line x1="42" y1="10" x2="36" y2="16"/><line x1="10" y1="42" x2="16" y2="36"/></g></svg>
</div>
<a class="btn about-btn">Contact us
  <svg width="18" height="14" viewBox="0 0 18 14"><path d="M1 7h15M10 1l6 6-6 6" fill="none" stroke="#fff" stroke-width="2"/></svg></a>

<section>
  <div class="section-head" style="top:1466px"><span class="eyebrow" style="position:relative">OUR SERVICES</span><h2>Services We Offer</h2></div>
  <article class="service" style="left:93px">
    <div class="photo" role="img" aria-label="Worker with ear protection trimming grass with a string trimmer" style="background:linear-gradient(170deg,#7fa653,#4f7b34 60%,#3d5e2a)"></div>
    <div class="cap-ic"><svg width="22" height="22" viewBox="0 0 24 24"><path d="M12 3l8 6-3 10H7L4 9z" fill="none" stroke="#fff" stroke-width="1.8"/></svg></div>
    <div class="cap">Landscape Design</div>
  </article>
  <article class="service featured" style="left:438px;width:319px">
    <div class="photo"></div>
    <svg style="position:absolute;left:126px;top:96px" width="68" height="60" viewBox="0 0 68 60"><path d="M34 6l24 16-9 30H19L10 22z" fill="none" stroke="#fff" stroke-width="3"/><g fill="var(--navy)" stroke="#fff" stroke-width="3"><circle cx="34" cy="6" r="4"/><circle cx="58" cy="22" r="4"/><circle cx="49" cy="52" r="4"/><circle cx="19" cy="52" r="4"/><circle cx="10" cy="22" r="4"/></g></svg>
    <h3>Irrigation Systems</h3>
    <p>Lorem ipsum dolor sit amet, conse ctetur adipiscing elit, sed do eius mod tempor incididunt ut labore et dolore magna aliqua.</p>
  </article>
  <article class="service" style="left:788px">
    <div class="photo" role="img" aria-label="Gardener in orange cap pruning a shrub" style="background:linear-gradient(170deg,#9cc270,#5f8c3c 55%,#3f6a2c)"></div>
    <div class="cap-ic"><svg width="22" height="22" viewBox="0 0 24 24"><path d="M12 3l8 6-3 10H7L4 9z" fill="none" stroke="#fff" stroke-width="1.8"/></svg></div>
    <div class="cap">Outdoor Lighting</div>
  </article>
</section>

<section>
  <div class="abs help" role="img" aria-label="Dim suburban house front behind a blue overlay"></div>
  <div class="abs help-circle"></div>
  <div class="abs help-photo" role="img" aria-label="Gardener in green cap kneeling with hedge shears"></div>
  <div class="help">
    <h2>NEED HELP? WE'RE<br>AVAILABLE 24/7</h2>
    <p>Call Us or submit a form below to speak with an expert today for a free quote</p>
  </div>
  <a class="btn help-btn">Contact us
    <svg width="18" height="14" viewBox="0 0 18 14"><path d="M1 7h15M10 1l6 6-6 6" fill="none" stroke="#fff" stroke-width="2"/></svg></a>
</section>

<section>
  <div class="abs reviews"></div>
  <div class="section-head" style="top:2492px"><span class="eyebrow" style="position:relative">TESTIMONIALS</span><h2>Clients' Reviews</h2></div>
  <div class="review" style="left:93px">Lorem ipsum dolor sit amet, consectetur adipiscing elit, sed do eiusmod tempor incididunt ut labore et dolore magna aliqua. Ut enim ad minim veniam.<span class="tail"></span></div>
  <div class="review active" style="left:437px">Lorem ipsum dolor sit amet, consectetur adipiscing elit, sed do eiusmod tempor incididunt ut labore et dolore magna aliqua. Ut enim ad minim veniam.<span class="tail"></span></div>
  <div class="review" style="left:783px">Lorem ipsum dolor sit amet, consectetur adipiscing elit, sed do eiusmod tempor incididunt ut labore et dolore magna aliqua. Ut enim ad minim veniam.<span class="tail"></span></div>
  <div class="person" style="left:93px"><div class="av" role="img" aria-label="Client portrait" style="background:#2a2f44"></div><div class="nm">Nora Hale</div><div class="rl">Engineer</div></div>
  <div class="person" style="left:437px"><div class="av" role="img" aria-label="Client portrait" style="background:#e9c14a"></div><div class="nm g">Nora Hale</div><div class="rl">Engineer</div></div>
  <div class="person" style="left:783px"><div class="av" role="img" aria-label="Client portrait" style="background:#d9dde3"></div><div class="nm">Nora Hale</div><div class="rl">Engineer</div></div>
  <div class="abs dots"><span class="on"></span><span></span><span></span><span></span></div>
</section>

<section>
  <div class="section-head" style="top:3095px"><span class="eyebrow" style="position:relative">CONTACT US</span><h2>Get un Touch with Us</h2></div>
  <div class="abs form-box">
    <h3>Get in touch</h3><span class="dash"></span>
    <div class="field" style="left:50px;top:76px;width:184px;height:36px">Your name*</div>
    <div class="field" style="left:254px;top:76px;width:184px;height:36px">Phone number...</div>
    <div class="field" style="left:50px;top:126px;width:388px;height:36px;justify-content:space-between;padding-right:16px">Choose Service*
      <svg width="10" height="6" viewBox="0 0 10 6"><path d="M1 1l4 4 4-4" fill="none" stroke="#d8dae8" stroke-width="1.4"/></svg></div>
    <div class="field" style="left:50px;top:176px;width:388px;height:98px;align-items:flex-start;padding-top:16px">Message...</div>
  </div>
  <a class="btn quote-btn" style="left:162px"><svg width="12" height="12" viewBox="0 0 24 24"><path d="M2 12l20-9-7 19-3-8z" fill="none" stroke="#fff" stroke-width="2"/></svg>Get a Quote</a>
  <div class="abs contact-photo" role="img" aria-label="Crew planting flowers in a front-yard garden bed beside a truck"></div>
</section>

<footer>
  <div class="abs footer" role="img" aria-label="Dark night-time aerial view of a road and trees"></div>
  <svg class="abs" style="left:0;top:3690px" width="1200" height="120" viewBox="0 0 1200 120">
    <path d="M0 0H1200V40 C1000 100 800 120 600 90 C400 55 200 40 0 90Z" fill="var(--white)"/>
    <path d="M0 90 C200 40 400 55 600 90 C800 120 1000 100 1200 40 L1200 52 C1000 118 800 136 600 104 C400 70 200 58 0 104Z" fill="var(--green)"/>
    <path d="M0 104 C200 58 400 70 600 104 C800 136 1000 118 1200 52 L1200 120 L0 120Z" fill="var(--footer)"/>
  </svg>
  <div class="abs foot-brand">Larchvale</div>
  <div class="foot-sep" style="left:416px"></div>
  <div class="foot-info" style="left:430px"><svg width="32" height="32" viewBox="0 0 32 32"><g fill="none" stroke="#e8e8ea" stroke-width="1.6"><circle cx="16" cy="16" r="14"/><ellipse cx="16" cy="16" rx="6" ry="14"/><path d="M2 16h28M5 8h22M5 24h22"/></g></svg><div>123, Building Name, Street<br>City, State XY 123456</div></div>
  <div class="foot-sep" style="left:668px"></div>
  <div class="foot-info" style="left:690px"><svg width="30" height="32" viewBox="0 0 30 32"><g fill="none" stroke="#e8e8ea" stroke-width="1.6"><rect x="2" y="2" width="16" height="28" rx="2"/><path d="M22 11c2 2 2 8 0 10M25 8c4 4 4 12 0 16"/></g></svg><div>PHONE<br>(555) 014 7788</div></div>
  <div class="foot-sep" style="left:846px"></div>
  <div class="foot-info" style="left:866px"><svg width="30" height="30" viewBox="0 0 30 30"><g fill="none" stroke="#e8e8ea" stroke-width="1.6"><rect x="2" y="7" width="26" height="20"/><path d="M2 7l13 11 13-11"/></g></svg><div>EMAIL<br>hello@larchvale.com</div></div>
  <div class="foot-rule" style="top:4034px"></div>
  <nav class="foot-nav">
    <a style="left:276px">HOME</a><a style="left:370px">SERVICES</a><a style="left:475px">ABOUT US</a><a style="left:594px">TESTIMONIALS</a><a style="left:745px">BLOG</a><a style="left:837px">CONTACT US</a>
  </nav>
  <div class="foot-rule" style="top:4084px"></div>
  <div class="abs copy">Larchvale</div>
  <span class="social" style="left:934px"></span><span class="social" style="left:967px"></span><span class="social" style="left:1000px"></span><span class="social" style="left:1033px"></span>
</footer>

</body>
</html>
```